Web Design Project (Mente Lumo)

We are going to do a therapy template to a psychologist. The site already exists, adress: www.mentelumo.net. So, its a total redesign job. I'm from Brazil, the language is PT-BR, so I'm gonna translate what you think be necessary. You can use the current structure from the website as a base to the new design. Check this template to see what I usually like: http://www.layoutkestrel.com/demo/51907.html
Updates

I'm waiting for new creative designs. The 'structure' image is just for 'pb'.

Requirements
Must have
• We need a modern menu, it should use a cool font style and make some kind of effect and little noise when the user pass over with the mouse (FLASH/HTML 5). The main page must emphasize the fact that we offer online treatment, like a picture or frame saying "Online Treatment, click here". It must also show the therapist picture and her name. The colors need to pass a tranquility feeling. The clinic telephone must always be present, doesn't matter which page the user is. The website must adapt to any resolution above 1024x768, crossbrowsing and accept javascript (I'll use www.slotvira.com, so its necessary embed code)
Nice to have
• I would appreciate if there was some kind of slow background animation, passing behind the text using the transparency.
Should not have
• Can't take too long to load, and won't have news or blog

```html
<!DOCTYPE html>
<html lang="pt-BR">
<head>
<meta charset="utf-8">
<title>Mente Lumo — Terapia Cognitiva</title>
<link rel="stylesheet" href="https://fonts.googleapis.com/css2?family=Alike&family=Rokkitt:wght@700&family=Arimo&display=swap">
<style>
:root{
  --dark:#1c2029;
  --dark-2:#252a34;
  --green:#84c121;
  --green-light:#98d03a;
  --blue:#2a7fc4;
  --blue-dark:#1d5f9a;
  --sky:#3fc0ef;
  --white:#ffffff;
  --text:#3a3a3a;
  --link:#2b80c5;
  --photo-bg:#dbe9bd;
}
*{margin:0;padding:0;box-sizing:border-box}
html,body{width:1200px;height:879px;overflow:hidden;background:var(--white)}
body{position:relative;font-family:"Arimo",Arial,sans-serif}
.site-header{position:absolute;left:0;top:0;width:1200px;height:100px;background:linear-gradient(#262b35,#171a21)}
.brand{position:absolute;left:138px;top:30px;display:flex;align-items:center;gap:10px;color:#cfe6b0;font-family:"Alike",serif;font-size:30px}
.brand-dot{width:30px;height:30px;border-radius:50%;background:#9fcf58}
.main-nav{position:absolute;left:414px;top:0;display:flex;height:100px}
.main-nav a{display:block;line-height:100px;padding:0 12px;color:var(--white);font-family:"Alike",serif;font-size:20px;text-decoration:none}
.main-nav a.active{background:var(--green);padding:0 17px;width:77px;text-align:center}
.hero{position:absolute;left:0;top:100px;width:1200px;height:321px;background:radial-gradient(circle at 550px 320px,var(--green-light),var(--green) 60%)}
.hero h1{position:absolute;left:138px;top:40px;font-family:"Alike",serif;font-weight:400;font-size:38px;color:var(--white);text-shadow:0 2px 3px rgba(0,0,0,.3)}
.hero p{position:absolute;left:138px;width:640px;font-family:"Alike",serif;font-size:18.5px;line-height:22px;color:var(--white);text-shadow:0 1px 2px rgba(0,0,0,.3)}
.hero .p1{top:112px}.hero .p2{top:222px}
.hero-art{position:absolute;left:789px;top:11px;width:272px;height:310px;border-radius:50% 45% 0 0;background:radial-gradient(circle at 55% 35%,#7fb0e8,#1f4f9c 70%)}
.tagline-band{position:absolute;left:0;top:421px;width:1200px;height:53px;background:var(--dark)}
.tagline{position:absolute;right:138px;top:18px;color:var(--white);font-family:"Rokkitt",serif;font-size:16px;letter-spacing:.5px}
.cta-online{position:absolute;left:138px;top:401px;width:294px;height:85px;border-radius:5px;background:linear-gradient(#3d95d8,var(--blue-dark));border-bottom:6px solid #164a78;color:var(--white);font-family:"Rokkitt",serif;font-size:23px;display:flex;align-items:center;padding-left:19px;gap:18px}
.cta-arrow{width:36px;height:36px;border-radius:50%;background:#1b5c95;border:2px solid #7ab8e8}
.profile-card{position:absolute;left:138px;top:498px;width:164px;height:245px;background:var(--photo-bg);text-align:center}
.profile-photo{margin:7px auto 0;width:148px;height:158px;background:linear-gradient(#8a8a8a,#4a4a4a)}
.profile-role{font-family:"Alike",serif;font-size:25px;color:#333;line-height:26px;margin-top:3px}
.profile-name{font-family:"Alike",serif;font-size:25px;color:var(--dark);line-height:24px;font-weight:700}
.profile-id{font-family:"Alike",serif;font-size:11px;color:#222;margin-top:3px}
.info-col{position:absolute;top:498px;width:218px;height:245px;border-left:1px dotted #999;padding-left:14px}
.info-col h2{font-family:"Alike",serif;font-weight:400;font-size:19px;color:var(--dark);margin:6px 0 16px}
.info-col h2 span{color:var(--link)}
.info-col p{font-size:13.5px;line-height:16.6px;color:var(--text)}
.info-col a{display:block;margin-top:16px;font-size:11px;color:var(--link);text-decoration:none}
.col-1{left:314px}.col-2{left:546px}
.col-divider{position:absolute;left:780px;top:498px;height:245px;border-left:1px dotted #999}
.side-btn{position:absolute;left:792px;width:269px;display:flex;align-items:center}
.side-btn .bar{position:absolute;left:40px;right:0;border-radius:4px;height:69px}
.side-btn .circle{position:relative;width:85px;height:85px;border-radius:50%;border:3px solid var(--white);z-index:1}
.side-btn .label{position:relative;z-index:1;margin-left:14px;color:var(--white);font-family:"Rokkitt",serif;font-size:25px;line-height:27px}
.btn-phone{top:481px}.btn-phone .bar{top:8px;background:linear-gradient(#5fd2f7,#22afe3)}
.btn-phone .circle{background:linear-gradient(#74d8f8,#1aa6dd);display:flex;align-items:center;justify-content:center}
.btn-online{top:570px}.btn-online .bar{top:8px;background:var(--green)}
.btn-online .circle{background:radial-gradient(#d8b49a,#8a6a55)}
.btn-map{top:658px}.btn-map .bar{top:7px;background:var(--dark)}
.btn-map .circle{background:radial-gradient(#4a4f5a,var(--dark))}
.site-footer{position:absolute;left:0;top:767px;width:1200px;height:112px;background:linear-gradient(#222731,#161920);color:var(--white)}
.footer-info{position:absolute;left:138px;top:21px;font-size:12px;line-height:18.5px}
.footer-info small{font-size:10px;color:#bbb}
.footer-brand{position:absolute;right:138px;top:34px;display:flex;align-items:center;gap:10px;color:#cfe6b0;font-family:"Alike",serif;font-size:28px}
</style>
</head>
<body>
<header class="site-header">
  <div class="brand"><span class="brand-dot"></span>Mente Lumo</div>
  <nav class="main-nav">
    <a class="active" href="#">Home</a><a href="#">Tratamentos</a><a href="#">Perguntas</a><a href="#">Consultório</a><a href="#">Localização</a><a href="#">Contato</a>
  </nav>
</header>
<section class="hero">
  <h1>O que é Terapia Cognitiva?</h1>
  <p class="p1">A Terapia Cognitiva tem como método a interpretação de processos e conteúdos mentais (as cognições), e sua influência na vida cotidiana. O comportamento e a emoção vêm depois do processamento cognitivo. É vital conhecermos nossos pensamentos para termos controle sobre eles.</p>
  <p class="p2">Todo distúrbio psíquico tem origem no pensamento. A Terapia Cognitiva educa através da busca de seu equilíbrio emocional....</p>
  <div class="hero-art" role="img" aria-label="Ilustração de cabeça humana azul em perfil com engrenagens no cérebro"></div>
</section>
<div class="tagline-band"><span class="tagline">É VITAL PARA SABER SEUS PENSAMENTOS ...</span></div>
<a class="cta-online">ONLINE TREATMENT
  <svg class="cta-arrow" viewBox="0 0 36 36"><path d="M15 10l8 8-8 8" fill="none" stroke="#fff" stroke-width="4"/></svg>
</a>
<div class="profile-card">
  <div class="profile-photo" role="img" aria-label="Foto da psicóloga"></div>
  <div class="profile-role">Psicóloga</div>
  <div class="profile-name">Clara Vilela</div>
  <div class="profile-id">CRP: 6/204518</div>
</div>
<article class="info-col col-1">
  <h2>Who am i? - <span>Perfil</span></h2>
  <p>Lorem ipsum dolor sit amet, consectetur adipisicing elit, sed do eiusmod tempor incididunt ut labore et dolore magna aliqua. Ut enim ad minim veniam, quis nostrud exercitation ullamco laboris nisi ut aliquip ex ea commodo consequat.</p>
  <a href="#">readmore →</a>
</article>
<article class="info-col col-2">
  <h2>Quem <span>somos?</span></h2>
  <p>Lorem ipsum dolor sit amet, consectetur adipisicing elit, sed do eiusmod tempor incididunt ut labore et dolore magna aliqua. Ut enim ad minim veniam, quis nostrud exercitation ullamco laboris nisi ut aliquip ex ea commodo consequat.</p>
  <a href="#">readmore →</a>
</article>
<div class="col-divider"></div>
<a class="side-btn btn-phone"><span class="bar"></span>
  <span class="circle"><svg width="40" height="48" viewBox="0 0 40 48"><path d="M10 4c3 0 5 8 5 10s-4 3-4 5 4 12 7 14 4-2 6-2 8 5 8 8-4 6-7 6C13 49 2 26 4 12 5 7 7 4 10 4z" fill="#fff"/></svg></span>
  <span class="label">(11) 5820-4936</span></a>
<a class="side-btn btn-online"><span class="bar"></span>
  <span class="circle" role="img" aria-label="Foto de paciente"></span>
  <span class="label">ONLINE<br>TREATMENT</span></a>
<a class="side-btn btn-map"><span class="bar"></span>
  <span class="circle" role="img" aria-label="Mapa-múndi"></span>
  <span class="label">MAP<br>LOCATION</span></a>
<footer class="site-footer">
  <div class="footer-info">Rua Alameda Serena, 412, 5º andar, Sala 21 - Centro - Vale Azul, SP<br>Clique aqui para ver o mapa<br>contato@mentelumo.net<br><small>Copyright © 2012 - Todos os direitos reservados</small></div>
  <div class="footer-brand"><span class="brand-dot"></span>Mente Lumo</div>
</footer>
</body>
</html>
```